Design Menu card and product signage within shop for Indian fast food outlet

we are Indian Cafe style shop based in Sydney called Spice Lantern Lane Eats.
we sell Indian street food,tea,sweets and other fast food from the outlet

we will provide you pictures of few products with prices and size of banners/which will be displayed within shop inside to enhance and grab customer attraction

Target Market(s)

Indians and other communites all age group

Requirements
Must have
• pictures of Samosas, Panipuri,chaat , dosa,momos sweets can be included in menu
Nice to have
• Earthtone color schemes will be preferred and not too dark colors

```html
<!DOCTYPE html>
<html lang="en">
<head>
<meta charset="utf-8">
<title>Spice Lantern Lane Eats – Hot Snacks Menu</title>
<link href="https://fonts.googleapis.com/css2?family=Roboto+Slab:wght@300;400&family=Great+Vibes&family=Montserrat:wght@500;600&family=Pathway+Gothic+One&family=Arimo&display=swap" rel="stylesheet">
<style>
  :root {
    --paper: #ffffff;
    --wood-dark: #3e2a1f;
    --wood-mid: #5a4030;
    --wood-light: #6b4d3a;
    --gold: #d9a845;
    --cream: #f4ece2;
    --muted: #d8ccbf;
    --saffron: #f08a2c;
    --leaf: #2f8f46;
    --plate: #f3f1ec;
    --fried: #b8732c;
    --caption: #333333;
  }
  * { box-sizing: border-box; margin: 0; padding: 0; }
  html, body { width: 1200px; height: 960px; overflow: hidden; background: var(--paper); }
  body { position: relative; font-family: "Roboto Slab", serif; }

  .page {
    position: absolute; top: 40px; width: 559px; height: 878px; overflow: hidden;
    background: linear-gradient(180deg, var(--wood-mid) 0%, var(--wood-light) 45%, var(--wood-mid) 75%, var(--wood-dark) 100%);
  }
  .page--inside { left: 38px; }
  .page--cover { left: 600px; }
  .frame {
    position: absolute; top: 43px; left: 47px; width: 467px; height: 803px;
    border: 3px solid var(--gold); box-shadow: 2px 3px 4px rgba(0,0,0,.45);
  }

  .menu-title {
    position: absolute; left: 78px; top: 90px; font-weight: 400;
    font-family: "Great Vibes", cursive; font-size: 27px; color: var(--cream);
  }
  .item { position: absolute; left: 75px; width: 420px; color: var(--cream); }
  .item__name { font-size: 14.5px; font-weight: 400; }
  .item__desc { font-size: 7.5px; line-height: 10px; color: var(--muted); font-weight: 300; margin-top: 3px; }
  .item__price { position: absolute; top: 2px; font-size: 14px; }
  .item__price small { font-size: 10.5px; color: var(--muted); }
  .onion-mark {
    display: inline-block; width: 28px; height: 12px; vertical-align: middle; margin-left: 6px;
    border-radius: 6px; background: linear-gradient(90deg, #e6d6cc, #b84a4a);
  }
  .dish { position: absolute; border-radius: 50%; box-shadow: 2px 4px 6px rgba(0,0,0,.45); }

  .plate-icon { position: absolute; left: 240px; top: 93px; }
  .badge-shape {
    position: absolute; left: 232px; top: 228px; width: 96px; height: 96px;
    border-radius: 50%; background: var(--saffron);
  }
  .stroke { position: absolute; left: 218px; width: 122px; border-radius: 3px 12px 12px 3px; }
  .stroke--saffron { top: 365px; height: 30px; background: var(--saffron); }
  .stroke--leaf { top: 412px; height: 26px; background: var(--leaf); }
  .brand-name {
    position: absolute; left: 60px; width: 440px; top: 446px; text-align: center;
    font-family: "Montserrat", sans-serif; font-weight: 500; color: var(--paper);
    font-size: 27px; line-height: 34px; white-space: nowrap;
  }
  .tagline {
    position: absolute; left: 60px; width: 440px; top: 533px; text-align: center;
    font-family: "Montserrat", sans-serif; font-weight: 500; font-size: 11px;
    letter-spacing: 1px; color: var(--paper);
  }
  .cover-word {
    position: absolute; left: 330px; top: 705px;
    font-family: "Pathway Gothic One", sans-serif; font-size: 84px; color: var(--paper);
  }

  .caption { position: absolute; font-family: "Arimo", sans-serif; font-size: 21px; color: var(--caption); white-space: nowrap; }
  .caption--inside { left: 168px; top: 928px; }
  .caption--cover { left: 685px; top: 928px; }
  .caption--height { left: 10px; top: 628px; transform-origin: 0 0; transform: rotate(-90deg); }
</style>
</head>
<body>

<section class="page page--inside">
  <div class="frame"></div>
  <h1 class="menu-title">Hot Snacks Menu</h1>

  <div class="item" style="top:133px"><div class="item__name">Samosa</div>
    <div class="item__desc">Fried pastry with a savoury filling made from spiced<br>potatoes and peas.<br>-No onions and garlic added <i class="onion-mark" role="img" aria-label="No onion and garlic symbol"></i></div>
    <div class="item__price" style="left:324px">$2.50 <small>(each)</small></div></div>

  <div class="item" style="top:201px"><div class="item__name">Kachori</div>
    <div class="item__desc">Fried pastry with a savoury filling made from lentils.<br>-No onions and garlic added <i class="onion-mark" role="img" aria-label="No onion and garlic symbol"></i></div>
    <div class="item__price" style="left:324px">$2.50 <small>(each)</small></div></div>

  <div class="item" style="top:268px"><div class="item__name">Bread Pakora</div>
    <div class="item__desc">Bread sandwiched with a savoury filling of potatoes and peas.<br>-No onions and garlic added <i class="onion-mark" role="img" aria-label="No onion and garlic symbol"></i></div>
    <div class="item__price" style="left:324px">$2.50 <small>(each)</small></div></div>

  <div class="item" style="top:335px"><div class="item__name">Chilli Pakora</div>
    <div class="item__desc">Long green chillies dipped in chickpea batter and fried.<br>-No onions and garlic added</div>
    <div class="item__price" style="left:324px">$2.50 <small>(each)</small></div></div>

  <div class="item" style="top:402px"><div class="item__name">Onion Pakora</div>
    <div class="item__desc">Onion sliced, dipped in chickpea batter<br>and fried to golden brown.</div>
    <div class="item__price" style="left:324px">$2.50 <small>(each)</small></div></div>

  <div class="item" style="top:470px"><div class="item__name">Medhu Vada</div>
    <div class="item__desc">South Indian fritter made from white urid lentil, usually made in<br>a doughnut shape, with a crispy exterior and soft interior.</div>
    <div class="item__price" style="left:324px">$2.50 <small>(each)</small></div></div>

  <div class="item" style="top:537px"><div class="item__name">Masala Vada</div>
    <div class="item__desc">Patties made by coarsely grinding soaked chana dal or<br>bengal gram (lentils) with spices, onions &amp; herbs.</div>
    <div class="item__price" style="left:321px">$2.50 <small>(each)</small></div></div>

  <div class="item" style="top:605px"><div class="item__name">Aloo Bonda</div>
    <div class="item__desc">Ball shaped fritters with a coating of chickpea batter filled<br>in with spiced potatoes.</div>
    <div class="item__price" style="left:321px">$2.50 <small>(each)</small></div></div>

  <div class="item" style="top:672px"><div class="item__name">Mix Pakora</div>
    <div class="item__desc">South Indian fritters of mixed vegetables such as cauliflower,<br>potatoes, capsicum, brinjal dipped in besan / chickpea flour<br>and fried till golden brown.</div>
    <div class="item__price" style="left:321px">$2.50 <small>(each)</small></div></div>

  <div class="item" style="top:751px"><div class="item__name">Paneer Puff</div>
    <div class="item__desc">Pastry Turnovers with a flaky golden crust with spicy<br>flavourful paneer (cottage cheese ) filling.</div>
    <div class="item__price" style="left:321px">$2.50 <small>(each)</small></div></div>

  <div class="dish" style="left:300px;top:210px;width:87px;height:70px;background:radial-gradient(circle,#7a3f22 0 30%,var(--plate) 32%)" role="img" aria-label="Photo of kachori with chutney on a white plate"></div>
  <div class="dish" style="left:284px;top:385px;width:88px;height:60px;background:radial-gradient(circle,var(--fried) 0 30%,var(--plate) 33%)" role="img" aria-label="Photo of onion pakora with chutneys on a white plate"></div>
  <div class="dish" style="left:307px;top:552px;width:85px;height:63px;background:radial-gradient(circle,var(--fried) 0 32%,var(--plate) 35%)" role="img" aria-label="Photo of masala vada with green chutney on a white plate"></div>
  <div class="dish" style="left:300px;top:720px;width:90px;height:68px;background:radial-gradient(circle,#ea8a3a 0 16%,#eee6dc 18% 55%,var(--plate) 58%)" role="img" aria-label="Photo of paneer puffs with dip on a white plate"></div>
</section>

<section class="page page--cover">
  <div class="frame"></div>

  <svg class="plate-icon" width="78" height="62" viewBox="0 0 78 62" aria-label="Plate and cutlery icon" role="img">
    <g fill="none" stroke="#fff" stroke-width="2.5">
      <circle cx="39" cy="31" r="20"/><circle cx="39" cy="31" r="15"/>
    </g>
    <g fill="#fff">
      <rect x="5" y="2" width="2" height="16"/><rect x="9" y="2" width="2" height="16"/><rect x="13" y="2" width="2" height="16"/>
      <rect x="4" y="16" width="12" height="5" rx="2"/><rect x="8.5" y="20" width="3" height="40"/>
      <ellipse cx="71" cy="12" rx="5" ry="10"/><rect x="69.5" y="20" width="3" height="40"/>
    </g>
  </svg>

  <div class="badge-shape" role="img" aria-label="Menu badge area"></div>

  <div class="stroke stroke--saffron" role="img" aria-label="Saffron brush stroke"></div>
  <div class="stroke stroke--leaf" role="img" aria-label="Green brush stroke"></div>

  <div class="brand-name">Spice Lantern Lane Eats</div>
  <div class="tagline">Fresh Street Bites Every Day</div>
  <div class="cover-word">Menu</div>

  <div class="dish" style="left:364px;top:88px;width:200px;height:200px;background:radial-gradient(circle,#b47a38 0 42%,var(--plate) 45%)" role="img" aria-label="Photo of samosas with chutneys on a white plate"></div>
  <div class="dish" style="left:-10px;top:220px;width:212px;height:208px;background:radial-gradient(circle,#b8732c 0 40%,var(--plate) 43%)" role="img" aria-label="Photo of bread pakora with tamarind and green chutney on a white plate"></div>
  <div class="dish" style="left:356px;top:490px;width:216px;height:208px;background:radial-gradient(circle,#ea8a3a 0 18%,#efe7dd 20% 62%,var(--plate) 65%)" role="img" aria-label="Photo of steamed momos with spicy dip on a white plate"></div>
  <div class="dish" style="left:-10px;top:592px;width:222px;height:212px;background:radial-gradient(circle,#8a3f1f 0 40%,var(--plate) 43%)" role="img" aria-label="Photo of aloo tikki with chutneys on a white plate"></div>
</section>

<div class="caption caption--height">11" inch hight</div>
<div class="caption caption--inside">7" inch width_inside pages</div>
<div class="caption caption--cover">7" inch width_Cover page of Menu</div>

</body>
</html>
```